NEED LABEL FOR PACKAGED DRINKING WATER BOTTLE

we are a new company who is into manufacturing of packaged drinking water bottles in 200 ml 500 ml and 1000 ml. we already have a label which we are using in our local market but we are introducing our 200ml bottle in inflight catering where our products will be seen, consumed by various age and origin of people who travel on flights. so we want a label which is simple and elegant.the bottle is a square bottle and label size would be 198 mm x 36 mm.you can use the label provided below for reference.and the bottle shape also is provided
Target Market(s)
flight passengers in domestic flights
Industry/Entity Type
It Company
Look and feel
Each slider illustrates characteristics of the customer's brand and the style your logo design should communicate.

```html
<!DOCTYPE html>
<html lang="en">
<head>
<meta charset="utf-8">
<title>Nirava Packaged Drinking Water – 200 mL Label</title>
<link rel="stylesheet" href="https://fonts.googleapis.com/css2?family=Cormorant+Garamond:wght@500;700&family=Arimo:wght@700&display=swap">
<style>
  :root {
    --canvas: #ffffff;
    --sky-light: #f4fbff;
    --sky-mid: #d6ecfa;
    --sky-deep: #b5dcf4;
    --brand-blue: #2f66b8;
    --tag-blue: #3a8fcf;
    --ink-navy: #123f86;
    --band-navy: #1d58ad;
    --band-light: #7fc0ea;
    --wave-deep: #2e74c0;
    --wave-foam: #cfe8f8;
    --drop-teal: #3fb0df;
  }
  * { margin: 0; padding: 0; box-sizing: border-box; }
  html, body {
    width: 1200px;
    height: 1049px;
    overflow: hidden;
    background: var(--canvas);
  }
  .canvas {
    position: relative;
    width: 1200px;
    height: 1049px;
  }
  .label {
    position: absolute;
    left: 50px;
    top: 424px;
    width: 1100px;
    height: 200px;
    overflow: hidden;
    background:
      radial-gradient(ellipse 60% 120% at 35% 10%, var(--sky-light) 0%, var(--sky-mid) 55%, var(--sky-deep) 100%);
    box-shadow: 0 2px 10px rgba(20, 60, 120, 0.12);
  }
  .splash-art {
    position: absolute;
    left: 0;
    top: 95px;
    width: 170px;
    height: 92px;
    background: radial-gradient(ellipse at 40% 60%, var(--wave-deep) 0%, rgba(120,180,230,0.6) 50%, rgba(214,236,250,0) 80%);
  }
  .wave-art {
    position: absolute;
    right: 0;
    bottom: 18px;
    width: 520px;
    height: 70px;
    background: linear-gradient(170deg, rgba(214,236,250,0) 20%, var(--wave-foam) 45%, var(--wave-deep) 100%);
    clip-path: polygon(0 100%, 30% 70%, 60% 40%, 85% 15%, 100% 0, 100% 100%);
  }
  .brand {
    position: absolute;
    left: 150px;
    top: 14px;
    display: flex;
    align-items: center;
    gap: 14px;
  }
  .brand-name {
    font-family: "Cormorant Garamond", serif;
    font-weight: 700;
    font-size: 82px;
    line-height: 1;
    color: var(--brand-blue);
  }
  .brand-dot {
    width: 30px;
    height: 30px;
    border-radius: 50%;
    background: var(--drop-teal);
  }
  .tagline {
    position: absolute;
    left: 232px;
    top: 104px;
    font-family: "Cormorant Garamond", serif;
    font-weight: 500;
    font-size: 28px;
    color: var(--tag-blue);
  }
  .net-content {
    position: absolute;
    left: 205px;
    top: 146px;
    font-family: "Arimo", sans-serif;
    font-weight: 700;
    font-size: 17px;
    color: var(--ink-navy);
  }
  .net-content small {
    font-size: 14px;
  }
  .band {
    position: absolute;
    left: 0;
    bottom: 0;
    width: 100%;
    height: 18px;
    background: var(--band-navy);
    border-top: 4px solid var(--band-light);
  }
</style>
</head>
<body>
  <main class="canvas">
    <section class="label" aria-label="Nirava 200 mL bottle label">
      <div class="splash-art" role="img" aria-label="Water splash illustration"></div>
      <div class="wave-art" role="img" aria-label="Blue water wave illustration"></div>
      <div class="brand">
        <span class="brand-name">Nirava</span>
        <span class="brand-dot"></span>
      </div>
      <p class="tagline">Packaged Drinking Water</p>
      <p class="net-content">NET 200mL <small>(12 fl.oz.)</small></p>
      <div class="band"></div>
    </section>
  </main>
</body>
</html>
```